Technology Ideation/Innovation Consultant-One Page (for now) Site Reflective Of Its Focus.

Based in Tampa, Florida...I offer my consulting services, along with my extensive network of companies and technologies, to people that are looking for new, novel, and innovative applications for their technology and/or companies & governmental agencies to identify solutions to their Existing Challenges and Future Needs. I then Identify Connections and/or Solutions between technologies and set up collaborations between the parties. I also run a Forum that allows people to present new, novel, and innovative technologies and capabilities to a broad audience for ideation and collaboration.

Logo Text

Marrowgate Concepts LLC

Coding

```html
<!DOCTYPE html>
<html lang="en">
<head>
<meta charset="utf-8">
<title>Marrowgate Concepts LLC</title>
<link rel="stylesheet" href="https://fonts.googleapis.com/css2?family=Poppins:wght@500;600;700&family=Lato:wght@400;700&display=swap">
<style>
:root{
  --blue:#0b6bc4;
  --blue-dark:#0756a3;
  --ink:#1b1b1b;
  --text:#5a5a5a;
  --muted:#9a9a9a;
  --panel:#f3f3f3;
  --field:#f2f3f5;
  --dark:#222222;
  --dark-2:#1d1d1d;
  --white:#ffffff;
}
*{box-sizing:border-box;margin:0;padding:0}
html,body{width:1200px;height:4687px;overflow:hidden}
body{position:relative;background:var(--white);font-family:"Lato",Arial,sans-serif;color:var(--text)}
.abs{position:absolute}
.eyebrow{font-family:"Lato",Arial,sans-serif;font-size:14px;letter-spacing:1px;color:var(--blue);text-transform:uppercase}
.h2{font-family:"Poppins",Arial,sans-serif;font-weight:700;color:var(--ink);font-size:31px;line-height:46px}
.body-text{font-size:12.5px;line-height:23.5px;color:var(--text)}
.btn{display:flex;align-items:center;justify-content:center;background:var(--blue);color:var(--white);font-family:"Poppins",Arial,sans-serif;font-weight:500;font-size:14px;border-radius:22px}

.site-header{left:0;top:0;width:1200px;height:77px;background:var(--white);border-bottom:1px solid #eee}
.brand{left:150px;top:14px;width:130px;font-family:"Poppins",Arial,sans-serif;font-weight:700;font-size:14px;line-height:17px;color:var(--blue)}
.nav{top:30px;font-family:"Poppins",Arial,sans-serif;font-weight:500;font-size:14px;color:var(--ink)}
.header-phone{left:767px;top:29px;font-size:15px;color:var(--blue);display:flex;align-items:center;gap:8px}

.hero{left:0;top:77px;width:1200px;height:548px;background:linear-gradient(100deg,#6e7a84 0%,#9aa7b0 35%,#b8c2c8 55%,#6f7d88 100%)}
.hero-shade{left:0;top:0;width:1200px;height:548px;background:rgba(20,30,40,.35)}
.hero-kicker{left:0;top:280px;width:1200px;text-align:center;color:var(--white);font-size:17px;letter-spacing:1px}
.hero-title{left:0;top:307px;width:1200px;text-align:center;color:var(--white);font-family:"Poppins",Arial,sans-serif;font-weight:600;font-size:50px;line-height:64px}

.about-photo{left:138px;top:694px;width:358px;height:386px;background:linear-gradient(135deg,#d9d2c8,#8a7a66 45%,#2c3f5e 75%,#d8dce2)}

.services{left:0;top:1158px;width:1200px;height:496px;background:var(--panel)}
.service{width:290px}
.service-icon{width:44px;height:44px;background:var(--blue);border-radius:4px;display:flex;align-items:center;justify-content:center}
.service-title{margin-top:28px;font-family:"Poppins",Arial,sans-serif;font-weight:600;font-size:20px;line-height:27px;color:var(--ink)}
.service-text{margin-top:10px;font-size:12.5px;line-height:20px;color:var(--text)}

.why-photo{left:118px;top:1708px;width:430px;height:423px;background:radial-gradient(circle at 55% 55%,#d8b59a 0%,#8b7a72 30%,#2d2d33 70%,#1a1a1f 100%)}
.feature-dot{width:14px;height:14px;border-radius:50%;background:#e6eef8;display:flex;align-items:center;justify-content:center}
.feature-title{font-weight:700;font-size:15px;color:var(--ink)}

.trust{left:118px;top:2254px;width:918px;height:315px;background:var(--dark-2)}
.trust-tab{left:865px;top:2212px;width:233px;height:194px;background:var(--blue);border-radius:30px 97px 97px 0}
.trust-tab p{color:var(--white);font-family:"Lato",Arial,sans-serif;font-size:19px;letter-spacing:1.2px;line-height:33.5px;padding:52px 0 0 31px}

.quote-mark{font-family:"Poppins",Arial,sans-serif;font-weight:700;font-size:56px;line-height:40px;color:var(--blue)}
.quote-lead{font-family:"Poppins",Arial,sans-serif;font-size:17.5px;line-height:34px;color:var(--ink)}
.stars{color:var(--blue);font-size:17px;letter-spacing:2px}
.dot{height:4px;border-radius:2px;background:#d6dbe2}

.forum-sub{font-weight:700;font-size:13px;line-height:22px;color:var(--ink)}
.forum-visual{left:605px;top:3156px;width:431px;height:455px}
.forum-block{left:0;top:91px;width:431px;height:364px;background:var(--blue);border-radius:0 0 200px 0}
.forum-figures{left:40px;top:20px;width:340px;height:435px;background:linear-gradient(180deg,#e9e6e2 0%,#d8d3cd 45%,#2a2c33 100%);border-radius:150px 150px 0 90px;opacity:.9}

.field-label{font-weight:700;font-size:13px;color:var(--ink)}
.field-label span{font-weight:400;color:var(--muted)}
.field{background:var(--field);height:42px;font-size:13px;color:var(--muted);padding:0 22px;display:flex;align-items:center}

.footer{left:0;top:4320px;width:1200px;height:367px;background:var(--dark)}
.footer-head{font-family:"Poppins",Arial,sans-serif;font-weight:600;font-size:13px;letter-spacing:1px;color:var(--white)}
.footer-link{font-size:15px;color:#d8d8d8}
.footer-small{font-size:11.5px;line-height:22px;color:#bdbdbd}
</style>
</head>
<body>

<header class="abs site-header">
  <div class="abs brand">Marrowgate Concepts LLC</div>
  <nav>
    <span class="abs nav" style="left:357px">Home</span>
    <span class="abs nav" style="left:433px">About</span>
    <span class="abs nav" style="left:510px">Services
      <svg width="9" height="6" viewBox="0 0 9 6" style="margin-left:2px"><path d="M1 1l3.5 3.5L8 1" fill="none" stroke="#1b1b1b" stroke-width="1.5"/></svg></span>
    <span class="abs nav" style="left:614px">Blog</span>
  </nav>
  <div class="abs header-phone">
    <svg width="18" height="18" viewBox="0 0 24 24"><path d="M6.6 10.8c1.4 2.8 3.8 5.1 6.6 6.6l2.2-2.2c.3-.3.7-.4 1-.2 1.1.4 2.3.6 3.6.6.6 0 1 .4 1 1V20c0 .6-.4 1-1 1C10.6 21 3 13.4 3 4c0-.6.4-1 1-1h3.5c.6 0 1 .4 1 1 0 1.3.2 2.5.6 3.6.1.3 0 .7-.2 1L6.6 10.8z" fill="none" stroke="#0b6bc4" stroke-width="1.6"/></svg>
    (813) 555-0142
  </div>
  <div class="abs btn" style="left:930px;top:22px;width:128px;height:38px">Lets Talk</div>
</header>

<section class="abs hero" role="img" aria-label="Photo of two colleagues laughing together in a bright modern office">
  <div class="abs hero-shade"></div>
</section>
<div class="abs hero-kicker">MARROWGATE CONCEPTS LLC</div>
<h1 class="abs hero-title">Igniting Innovation And<br>Collaboration</h1>
<div class="abs btn" style="left:535px;top:464px;width:128px;height:44px">Lets Talk</div>
<svg class="abs" style="left:0;top:555px" width="1200" height="75" viewBox="0 0 1200 75">
  <path d="M0 62 L600 12 L1200 62 L1200 75 L0 75 Z" fill="#0b6bc4"/>
  <path d="M0 70 L600 22 L1200 70 L1200 75 L0 75 Z" fill="#ffffff"/>
</svg>

<section>
  <div class="abs about-photo" role="img" aria-label="Photo of two businessmen reviewing a laptop together"></div>
  <div class="abs eyebrow" style="left:601px;top:695px">About Us</div>
  <h2 class="abs h2" style="left:601px;top:718px">Marrowgate Concepts LLC</h2>
  <p class="abs body-text" style="left:601px;top:792px;width:418px">Marrowgate Concepts LLC is a leading consulting firm based in Tampa, Florida. With a passion for innovation and a vast network of companies and technologies, we specialize in providing consulting services to individuals, companies, and governmental agencies seeking fresh, groundbreaking applications for their existing technology or assistance in identifying solutions for their current challenges and future needs. Our expertise lies in identifying connections and solutions between technologies, fostering collaborations, and facilitating ideation and collaboration through our dedicated forum.</p>
  <div class="abs" style="left:592px;top:1040px;height:24px;padding:0 8px;border-radius:12px;background:#eef3fa;font-family:'Poppins',Arial,sans-serif;font-size:13.5px;color:var(--blue-dark);display:flex;align-items:center;gap:6px">Learn more
    <svg width="12" height="10" viewBox="0 0 12 10"><path d="M1 5h9M6.5 1.5L10 5 6.5 8.5" fill="none" stroke="#0b6bc4" stroke-width="1.5"/></svg></div>
</section>

<section class="abs services">
  <div class="abs eyebrow" style="left:0;top:50px;width:1200px;text-align:center">Consulting Services</div>
  <h2 class="abs h2" style="left:0;top:76px;width:1200px;text-align:center">Innovative Consulting Solutions For<br>Technology-Driven Clients</h2>

  <div class="abs service" style="left:127px;top:217px">
    <div class="service-icon"><svg width="24" height="24" viewBox="0 0 24 24"><circle cx="12" cy="10" r="6" fill="none" stroke="#fff" stroke-width="1.6"/><path d="M9 18h6M10 21h4" stroke="#fff" stroke-width="1.6"/></svg></div>
    <div class="service-title">Technology Application<br>Discovery</div>
    <p class="service-text">Unleash your tech's potential. Collaborate with us to uncover game-changing applications. Stay ahead in the tech landscape with our innovative insights.</p>
  </div>
  <div class="abs service" style="left:452px;top:217px">
    <div class="service-icon"><svg width="24" height="24" viewBox="0 0 24 24"><rect x="4" y="4" width="16" height="16" rx="2" fill="none" stroke="#fff" stroke-width="1.6"/><path d="M8 15l3-3 2 2 3-4" fill="none" stroke="#fff" stroke-width="1.6"/></svg></div>
    <div class="service-title">Strategic Solutions For<br>Challenges</div>
    <p class="service-text">Overcome obstacles, future-proof operations. Our tailored strategies address current needs and anticipate the future. Success through industry expertise.</p>
  </div>
  <div class="abs service" style="left:768px;top:217px">
    <div class="service-icon"><svg width="24" height="24" viewBox="0 0 24 24"><circle cx="8" cy="9" r="3" fill="none" stroke="#fff" stroke-width="1.6"/><circle cx="16" cy="9" r="3" fill="none" stroke="#fff" stroke-width="1.6"/><path d="M3 20c1-4 9-4 9 0M12 20c1-4 9-4 9 0" fill="none" stroke="#fff" stroke-width="1.6"/></svg></div>
    <div class="service-title">Collaborative Innovation<br>Facilitation</div>
    <p class="service-text">Ignite collaboration, drive innovation. Partner with us to foster transformative connections. Our forum fuels groundbreaking advancements.</p>
  </div>
</section>

<section>
  <div class="abs why-photo" role="img" aria-label="Photo of a hand touching a glowing network of connected people icons"></div>
  <div class="abs eyebrow" style="left:652px;top:1715px">Why Us</div>
  <h2 class="abs h2" style="left:652px;top:1738px">Network Of Companies<br>And Technologies</h2>

  <div class="abs feature-dot" style="left:652px;top:1855px"><svg width="6" height="8" viewBox="0 0 6 8"><path d="M1 1l3 3-3 3" fill="none" stroke="#0b6bc4" stroke-width="1.4"/></svg></div>
  <div class="abs feature-title" style="left:684px;top:1852px">Extensive Network</div>
  <p class="abs body-text" style="left:684px;top:1882px;width:350px;font-size:12px;line-height:20px">Tap into our vast network of companies and technologies for strategic connections and opportunities.</p>

  <div class="abs feature-dot" style="left:652px;top:1951px"><svg width="6" height="8" viewBox="0 0 6 8"><path d="M1 1l3 3-3 3" fill="none" stroke="#0b6bc4" stroke-width="1.4"/></svg></div>
  <div class="abs feature-title" style="left:684px;top:1948px">Resource and Expertise Access</div>
  <p class="abs body-text" style="left:684px;top:1978px;width:350px;font-size:12px;line-height:20px">Gain access to cutting-edge technologies and the right expertise to enhance your competitive edge.</p>

  <div class="abs feature-dot" style="left:652px;top:2047px"><svg width="6" height="8" viewBox="0 0 6 8"><path d="M1 1l3 3-3 3" fill="none" stroke="#0b6bc4" stroke-width="1.4"/></svg></div>
  <div class="abs feature-title" style="left:684px;top:2044px">Empower Competitive Advantage</div>
  <p class="abs body-text" style="left:684px;top:2074px;width:350px;font-size:12px;line-height:20px">Leverage our network to explore partnerships, access emerging technologies, and stay ahead in your industry.</p>
</section>

<section>
  <div class="abs trust"></div>
  <div class="abs trust-tab"><p>INNOVATIVE<br>COLLABORATIVE<br>CONNECTIONS</p></div>
  <div class="abs eyebrow" style="left:191px;top:2294px">Trust Us</div>
  <h2 class="abs h2" style="left:191px;top:2318px;color:#fff">Collaborations And Partnerships</h2>
  <p class="abs body-text" style="left:191px;top:2377px;width:580px;color:#d6d6d6">One of our core strengths is identifying and facilitating collaborations and partnerships between diverse parties. We believe that meaningful collaborations can drive innovation and propel the realization of groundbreaking ideas.</p>
  <div class="abs btn" style="left:191px;top:2482px;width:128px;height:44px">Lets Talk</div>
</section>

<section>
  <div class="abs eyebrow" style="left:0;top:2667px;width:1200px;text-align:center">Testimonials</div>
  <h2 class="abs h2" style="left:0;top:2690px;width:1200px;text-align:center">What Our Clients Have To Say</h2>

  <div class="abs" style="left:118px;top:2782px;width:460px">
    <div class="quote-mark">&ldquo;</div>
    <p class="quote-lead" style="margin-top:12px">&ldquo;Lorem Ipsum Dolor Sit Amet Consectetur<br>Lit Imperdiet Pharetra Diam Leo</p>
    <p class="body-text" style="margin-top:12px;font-size:12px">Gravida molestie quis suspendisse sem et velit convallis. Pretium accumsan et suspendisse neque malesuada vulputate cursus congue convallis. Vestibulum quis elit nec ac aliquam ac nibh mauris adipiscing.&rdquo;</p>
    <div class="stars" style="margin-top:20px">★★★★★</div>
    <div style="margin-top:4px;font-size:12.5px;color:var(--ink)">Dana Ellery</div>
  </div>
  <div class="abs" style="left:619px;top:2782px;width:460px">
    <div class="quote-mark">&ldquo;</div>
    <p class="quote-lead" style="margin-top:12px">&ldquo;Lorem Ipsum Dolor Sit Amet Consectetur<br>Lit Imperdiet Pharetra Diam Leo</p>
    <p class="body-text" style="margin-top:12px;font-size:12px">Gravida molestie quis suspendisse sem et velit convallis. Pretium accumsan et suspendisse neque malesuada vulputate cursus congue convallis. Vestibulum quis elit nec ac aliquam ac nibh mauris adipiscing.&rdquo;</p>
    <div class="stars" style="margin-top:20px">★★★★★</div>
    <div style="margin-top:4px;font-size:12.5px;color:var(--ink)">Dana Ellery</div>
  </div>

  <div class="abs dot" style="left:554px;top:3117px;width:26px"></div>
  <div class="abs dot" style="left:586px;top:3117px;width:26px;background:var(--blue)"></div>
  <div class="abs dot" style="left:620px;top:3117px;width:26px"></div>
</section>

<section>
  <div class="abs eyebrow" style="left:118px;top:3242px">Forum</div>
  <h2 class="abs h2" style="left:118px;top:3266px">Ideation And<br>Collaboration Forum</h2>
  <div class="abs forum-sub" style="left:118px;top:3384px">Platform for Open Innovation and Collaboration</div>
  <p class="abs body-text" style="left:118px;top:3412px;width:360px;font-size:12px;line-height:20px">Our dedicated forum serves as a platform for individuals and organizations to showcase their new, novel, and innovative technologies and capabilities.</p>
  <div class="abs" style="left:118px;top:3492px;width:36px;height:3px;background:var(--blue)"></div>
  <div class="abs forum-sub" style="left:118px;top:3511px;width:360px">Dynamic and Inclusive Environment for Transformative<br>Breakthroughs</div>
  <p class="abs body-text" style="left:118px;top:3564px;width:360px;font-size:12px;line-height:20px">Our forum fosters a dynamic and inclusive environment, encouraging active participation from a broad audience.</p>

  <div class="abs forum-visual" role="img" aria-label="Photo of a young man and woman reviewing a notebook in front of a blue panel">
    <div class="abs forum-block"></div>
    <div class="abs forum-figures"></div>
  </div>
</section>

<section>
  <div class="abs eyebrow" style="left:0;top:3689px;width:1200px;text-align:center">Lets Talk</div>
  <h2 class="abs h2" style="left:0;top:3706px;width:1200px;text-align:center">Get In Touch</h2>
  <p class="abs body-text" style="left:395px;top:3759px;width:410px;text-align:center;font-size:12.5px">Contact us today and let's explore the possibilities of unlocking your technology's full potential.</p>

  <div class="abs field-label" style="left:211px;top:3834px">Your name</div>
  <div class="abs field" style="left:211px;top:3864px;width:375px">Nora Fielding</div>
  <div class="abs field-label" style="left:611px;top:3834px">Your Phone</div>
  <div class="abs field" style="left:611px;top:3864px;width:374px">(727) 555-0193</div>

  <div class="abs field-label" style="left:211px;top:3934px">Your email</div>
  <div class="abs field" style="left:211px;top:3964px;width:375px">ravi.okafor@northmail.com</div>
  <div class="abs field-label" style="left:611px;top:3934px">Company name <span>(optional)</span></div>
  <div class="abs field" style="left:611px;top:3964px;width:374px">Brightfold</div>

  <div class="abs field-label" style="left:211px;top:4033px">Your email</div>
  <div class="abs field" style="left:211px;top:4063px;width:774px;height:127px;align-items:flex-start;padding-top:14px">Type your message here</div>

  <div class="abs btn" style="left:535px;top:4221px;width:128px;height:42px">Lets Talk</div>
</section>

<footer class="abs footer">
  <div class="abs" style="left:110px;top:100px;width:150px;font-family:'Poppins',Arial,sans-serif;font-weight:700;font-size:14px;line-height:18px;color:var(--white)">Marrowgate Concepts LLC</div>
  <div class="abs" style="left:110px;top:197px;width:36px;height:3px;background:var(--blue)"></div>
  <p class="abs footer-small" style="left:110px;top:218px;width:220px">Marrowgate Concepts LLC is a leading consulting firm based in Tampa, Florida.</p>

  <div class="abs footer-head" style="left:481px;top:65px">FOLLOW US</div>
  <div class="abs footer-link" style="left:481px;top:106px;display:flex;align-items:center;gap:14px"><svg width="14" height="14"><circle cx="7" cy="7" r="6" fill="none" stroke="#0b6bc4" stroke-width="1.5"/></svg>Photo Feed</div>
  <div class="abs footer-link" style="left:481px;top:141px;display:flex;align-items:center;gap:14px"><svg width="14" height="14"><circle cx="7" cy="7" r="6" fill="none" stroke="#0b6bc4" stroke-width="1.5"/></svg>Community</div>
  <div class="abs footer-link" style="left:481px;top:174px;display:flex;align-items:center;gap:14px"><svg width="14" height="14"><circle cx="7" cy="7" r="6" fill="none" stroke="#0b6bc4" stroke-width="1.5"/></svg>Updates</div>

  <div class="abs footer-head" style="left:668px;top:65px">QUICK LINKS</div>
  <div class="abs footer-link" style="left:668px;top:110px">Home</div>
  <div class="abs footer-link" style="left:668px;top:141px">About</div>
  <div class="abs footer-link" style="left:668px;top:172px">Services</div>
  <div class="abs footer-link" style="left:668px;top:203px">Blog</div>
  <div class="abs footer-link" style="left:668px;top:234px">Lets Talk</div>

  <div class="abs footer-head" style="left:850px;top:65px">CONTACT</div>
  <div class="abs footer-link" style="left:850px;top:122px;display:flex;align-items:center;gap:14px;font-size:16px">
    <svg width="16" height="16" viewBox="0 0 24 24"><path d="M6.6 10.8c1.4 2.8 3.8 5.1 6.6 6.6l2.2-2.2c.3-.3.7-.4 1-.2 1.1.4 2.3.6 3.6.6.6 0 1 .4 1 1V20c0 .6-.4 1-1 1C10.6 21 3 13.4 3 4c0-.6.4-1 1-1h3.5c.6 0 1 .4 1 1 0 1.3.2 2.5.6 3.6.1.3 0 .7-.2 1L6.6 10.8z" fill="#0b6bc4"/></svg>(813) 555-0177</div>
  <div class="abs footer-link" style="left:850px;top:158px;display:flex;align-items:center;gap:14px;font-size:16px">
    <svg width="16" height="12" viewBox="0 0 16 12"><rect width="16" height="12" rx="1.5" fill="#0b6bc4"/><path d="M1 1.5l7 5 7-5" fill="none" stroke="#222" stroke-width="1.3"/></svg>hello@marrowgatemail.com</div>

  <div class="abs" style="left:110px;top:302px;width:980px;height:1px;background:#3c3c3c"></div>
  <div class="abs" style="left:0;top:326px;width:1200px;text-align:center;font-size:13px;color:#cfcfcf">Copyright Marrowgate Concepts LLC I All rights reserved</div>
</footer>

</body>
</html>
```